Kaffeerösterei sucht Etiketten-Design
- schnelle Ausführung - mein Geschmack voll getroffen - unkompliziert und Kunden orientiert bei der Ausführung
Zielgruppe
Kaffeerösterei für die edelsten und teuersten Rohkaffees.
Meine Kunden sind Kaffee Geniesser.
Aufgabenstellung
Transparente Aufkleber für eine Schiefertafel im Format 22.5 cm x 15.5 cm.
Im Hand-Lettering Stil.
5 Schiefertafeln sind gewünscht.
Tafel 1
Kostenlos zur Degustation
Espresso
Café Crème 3.--
Americano 3.--
Filter Kaffee 3.--
Tafel 2
Kaffee & Milch
Cappuccino 4.--
Café Latte 4.--
Flat White 4.--
Latte Macchiato 4.--
Latte Macchiato mit Aroma 5.--
Kaffee & Hafermilch + 1.--
Tafel 3
Crepes
Pikant
- Pizza Crepes 7.--
- Flammkuchen Crepes 7.--
Süss
- Schoggi Crepes 6.--
- Apfelmus & Zimtzucker 6.--
Tafel 4
Kaffee & Schnaps
- Original Entlebucher Schwarzes 7.--
- Espresso Coretto 5.00
- Schwarzes mit Rahmhaube 8.--
Tafel 5
Schokolade & Milch
- heisse Schoggi 5.--
- heisse Schoggi mit Rahmhaube 6.--
- heisse Schoggi mit Espresso 6.--
- Schokolade & Hafermilch +1.--
Als Idee, was mir gefallen könnte:
https://www.bildsammlung.example/pin/104857392018374655/
https://de.grafikhort.example/vektorkunst/4418203-set-kaffeekarte-mit-tassen-kaffeegetranken-im-vintage-stil-stilisierte-zeichnung-mit-kreide-auf-tafel-schriftzug-sample-drinks
https://www.fotolager.example/stockfoto-heisser-kakao-bar-warm-hier-oben-hand-tafel-caf-schild-an-tafel-hintergrund-mit-farbe-kreide-schriftzug-werbung-fur-heisse-d-583021746.html

```html
<!DOCTYPE html>
<html lang="de">
<head>
<meta charset="utf-8">
<title>Kaffee &amp; Schnaps – Tafel 4</title>
<link rel="stylesheet" href="https://fonts.googleapis.com/css2?family=Amatic+SC:wght@700&family=Kaushan+Script&display=swap">
<style>
  :root {
    --paper: #ffffff;
    --slate: #1d1d1b;
    --cream: #fffbe0;
    --price: #fce8cc;
    --gold: #fbc76a;
    --line: #fdd27d;
    --chalk: #ffffff;
    --lilac: #bfa3cc;
  }
  html, body {
    margin: 0;
    padding: 0;
    width: 1200px;
    height: 874px;
    overflow: hidden;
    background: var(--paper);
  }
  .board {
    position: absolute;
    left: 63px;
    top: 63px;
    width: 1076px;
    height: 741px;
    background: var(--slate);
  }
  .canvas {
    position: relative;
    width: 1200px;
    height: 874px;
  }
  .title {
    position: absolute;
    left: 0;
    width: 1194px;
    top: 108px;
    margin: 0;
    text-align: center;
    font-family: "Kaushan Script", cursive;
    font-weight: 400;
    font-size: 86px;
    line-height: 1;
    color: var(--cream);
    letter-spacing: 1px;
  }
  .title .amp { color: var(--gold); }
  .flourish {
    position: absolute;
    top: 156px;
    width: 86px;
    height: 40px;
    border-radius: 20px;
    background: linear-gradient(90deg, rgba(251,199,106,0.25), rgba(251,199,106,0.45));
  }
  .flourish--left { left: 120px; }
  .flourish--right { left: 997px; }
  .menu-line {
    position: absolute;
    right: 323px;
    margin: 0;
    font-family: "Amatic SC", cursive;
    font-weight: 700;
    font-size: 74px;
    line-height: 1;
    letter-spacing: 2px;
    color: var(--chalk);
    white-space: nowrap;
  }
  .price {
    position: absolute;
    left: 912px;
    margin: 0;
    font-family: "Kaushan Script", cursive;
    font-size: 60px;
    line-height: 1;
    color: var(--price);
    white-space: nowrap;
  }
  .mug-art {
    position: absolute;
    left: 137px;
    top: 389px;
    width: 212px;
    height: 317px;
    border-radius: 24px 24px 60px 60px;
    background: linear-gradient(180deg, rgba(255,255,255,0.08) 0%, rgba(255,255,255,0.14) 60%, rgba(191,163,204,0.7) 100%);
  }
  .underline {
    position: absolute;
    left: 360px;
    top: 724px;
  }
</style>
</head>
<body>
<div class="canvas">
  <div class="board"></div>

  <div class="flourish flourish--left" role="img" aria-label="Goldene Schnörkel-Verzierung"></div>
  <h1 class="title">Kaffee <span class="amp">&amp;</span> Schnaps</h1>
  <div class="flourish flourish--right" role="img" aria-label="Goldene Schnörkel-Verzierung"></div>

  <p class="menu-line" style="top:278px">Original Entlebucher</p>
  <p class="menu-line" style="top:345px">Schwarzes</p>
  <p class="price" style="top:348px">7,–</p>

  <p class="menu-line" style="top:441px">Espresso Coretto</p>
  <p class="price" style="top:443px">5,–</p>

  <p class="menu-line" style="top:537px">Schwarzes</p>
  <p class="menu-line" style="top:603px">mit Rahmhaube</p>
  <p class="price" style="top:606px">8,–</p>

  <div class="mug-art" role="img" aria-label="Kreidezeichnung einer dampfenden Kaffeetasse auf lila Untertasse"></div>

  <svg class="underline" width="482" height="20" viewBox="0 0 482 20" aria-hidden="true">
    <path d="M2 10 C 120 2, 360 2, 480 12 C 360 10, 120 10, 8 14 Z" fill="var(--line)"/>
  </svg>
</div>
</body>
</html>
```